Need a business card for our overland brand!

We had the logo made and we need a great design for our business card. Use the logo provide or tweak it however you see fit.

Contact Information for Business Card

Name, Title, Telephone, email, website

```html
<!DOCTYPE html>
<html lang="en">
<head>
<meta charset="utf-8">
<title>Summit Trailways – Business Card</title>
<link rel="stylesheet" href="https://fonts.googleapis.com/css2?family=Montserrat:wght@400;500;700&display=swap">
<style>
  :root {
    --page-bg: #e6e8e7;
    --card-white: #f3f3f3;
    --navy: #1e2e45;
    --teal: #1b8fa8;
    --ink: #24364d;
    --light-grey: #d9d9d9;
  }
  * { box-sizing: border-box; margin: 0; padding: 0; }
  html, body {
    width: 1200px;
    height: 1200px;
    overflow: hidden;
    background: var(--page-bg);
    font-family: "Montserrat", sans-serif;
  }
  .sheet {
    width: 1200px;
    height: 1200px;
    display: flex;
    flex-direction: column;
    align-items: center;
    justify-content: center;
    gap: 60px;
  }
  .card {
    position: relative;
    width: 880px;
    height: 503px;
    border-radius: 4px;
    box-shadow: 0 6px 18px rgba(0, 0, 0, 0.12);
  }
  .card--front { background: var(--card-white); }
  .card--back {
    background: var(--navy);
    display: flex;
    align-items: center;
    justify-content: center;
  }
  .person {
    position: absolute;
    left: 78px;
    top: 80px;
  }
  .person__name {
    font-size: 36px;
    font-weight: 700;
    color: var(--teal);
    line-height: 1.1;
  }
  .person__title {
    margin-top: 8px;
    font-size: 23px;
    font-weight: 400;
    color: var(--ink);
  }
  .brand-name {
    font-weight: 700;
    text-transform: uppercase;
    line-height: 1.02;
  }
  .card--front .brand-name {
    position: absolute;
    right: 78px;
    top: 88px;
    text-align: right;
    font-size: 40px;
    color: var(--navy);
  }
  .card--back .brand-name {
    text-align: center;
    font-size: 96px;
    color: var(--light-grey);
    letter-spacing: 1px;
  }
  .contact {
    position: absolute;
    left: 78px;
    right: 78px;
    bottom: 62px;
    font-size: 22px;
    color: var(--ink);
  }
  .contact__item {
    display: flex;
    align-items: center;
    gap: 12px;
    height: 33px;
  }
  .contact__item svg {
    width: 20px;
    height: 20px;
    flex: none;
  }
  .contact__web {
    position: absolute;
    right: 0;
    bottom: 0;
  }
</style>
</head>
<body>
<main class="sheet">
  <section class="card card--front">
    <div class="person">
      <h1 class="person__name">Dane Porter</h1>
      <p class="person__title">Founder &amp; Director</p>
    </div>
    <p class="brand-name">Summit<br>Trailways</p>
    <div class="contact">
      <div class="contact__item">
        <svg viewBox="0 0 24 24" aria-hidden="true"><path fill="var(--teal)" d="M6.6 10.8a15 15 0 0 0 6.6 6.6l2.2-2.2c.3-.3.7-.4 1-.2 1.1.4 2.3.6 3.6.6.6 0 1 .4 1 1V20c0 .6-.4 1-1 1A17 17 0 0 1 3 4c0-.6.4-1 1-1h3.5c.6 0 1 .4 1 1 0 1.3.2 2.5.6 3.6.1.3 0 .7-.2 1z"/></svg>
        <span>(555)-204-7391</span>
      </div>
      <div class="contact__item">
        <svg viewBox="0 0 24 24" aria-hidden="true"><rect x="2" y="5" width="20" height="14" rx="1.5" fill="var(--teal)"/><path d="M3 6.5l9 6.5 9-6.5" fill="none" stroke="var(--card-white)" stroke-width="1.6"/></svg>
        <span>info@summittrailways.com</span>
      </div>
      <div class="contact__item contact__web">
        <svg viewBox="0 0 24 24" aria-hidden="true"><circle cx="12" cy="12" r="10" fill="var(--teal)"/><g fill="none" stroke="var(--card-white)" stroke-width="1.4"><ellipse cx="12" cy="12" rx="4" ry="10"/><path d="M2 12h20M12 2v20"/></g></svg>
        <span>www.summittrailways.com</span>
      </div>
    </div>
  </section>
  <section class="card card--back">
    <p class="brand-name">Summit<br>Trailways</p>
  </section>
</main>
</body>
</html>
```